An organizational wellness program flyer - The TALON Program flyer

Need a 2 page PDF and/or tri-fold marketing piece for a program that will be marketed to mid-large employer groups (100-5000 employees). The program is designed to reduce healthcare costs by providing knowledge, tools and techniques to increase employee self-awareness and self-agency. The program details are provided in the uploaded files.
Use the phrase "How much is chronic stress and burnout costing your organization?" as a headline
The designs should highlight the ROI through reduced healthcare costs, employee turnover and absenteeism and increased employee health and engagement.
The description of the TALON acronym should be included and prominent The "Tracks Across Life, Openness and Nurture".
Include The TALON Program framework
Do not include the details of the pathways. Only include the Pathway heading/title.
Have also provided scripts from marketing videos to inform what's included on the flyer, but do not include the scripts on the brochure.
Looking for something clean, not too text heavy but includes the right data points.
Include the phrase "This is not just a program. It's a paradigm shift." at the
Would like all of the source data files so that I can modify later if needed.
Include the BrindleCove logo on the brochure. www.brindlecove.com for brand colors.
organizations with 100-5000 employees; organizations looking for wellness programs
- Clean, compelling visuals
- Images of me on the brochure

```html
<!DOCTYPE html>
<html lang="en">
<head>
<meta charset="utf-8">
<title>The TALON Program – Flyer</title>
<link rel="stylesheet" href="https://fonts.googleapis.com/css2?family=Archivo+Black&family=Archivo:wght@300;400;500;600;700&family=Oswald:wght@500;600&display=swap">
<style>
  :root {
    --gold: #dfc35a;
    --gold-text: #d9bd55;
    --charcoal: #3a3a3a;
    --ink: #1f1f1f;
    --grey: #7b7b7d;
    --grey-light: #bdbdbf;
    --paper: #ffffff;
  }
  * { box-sizing: border-box; margin: 0; padding: 0; }
  html, body { width: 1200px; height: 727px; overflow: hidden; background: var(--paper); }
  body { position: relative; font-family: "Archivo", Arial, sans-serif; color: var(--ink); }

  .page { position: absolute; top: 74px; width: 446px; height: 577px; background: var(--paper); overflow: hidden; }
  .page--front { left: 126px; }
  .page--back { left: 631px; }

  /* Front page */
  .hero { position: absolute; left: 0; top: 0; width: 446px; height: 237px; background: var(--charcoal); }
  .hero__photo { position: absolute; left: 222px; top: 0; width: 224px; height: 237px;
    background: linear-gradient(160deg, #4a4a4c 0%, #5a6b8c 45%, #46557a 70%, #d9d9d9 100%); }
  .hero__headline { position: absolute; left: 22px; top: 14px; font-family: "Archivo Black", Arial, sans-serif;
    font-size: 27.5px; line-height: 31.5px; color: var(--gold-text); }
  .hero__lede { position: absolute; left: 23px; top: 183px; width: 180px; font-size: 9.2px; line-height: 11.4px;
    font-weight: 600; color: #fff; }

  .benefit-band { position: absolute; left: 0; top: 237px; width: 446px; height: 46px; background: var(--gold);
    display: flex; align-items: center; padding-left: 17px; gap: 0; }
  .benefit { display: flex; align-items: center; gap: 6px; width: 142px; }
  .benefit__icon { width: 29px; height: 29px; border-radius: 5px; background: var(--charcoal); flex: none; }
  .benefit__label { font-family: "Oswald", Arial, sans-serif; font-weight: 600; font-size: 11.3px; line-height: 14px; color: var(--charcoal); }

  .pathways-tab { position: absolute; left: 217px; top: 283px; width: 229px; height: 17px; background: var(--charcoal);
    border-bottom-left-radius: 4px; color: #fff; font-size: 11.5px; font-weight: 300; line-height: 17px; padding-left: 10px; }

  .benefits-chart { position: absolute; left: 8px; top: 281px; width: 194px; height: 194px; overflow: visible; }
  .chart-label { position: absolute; font-size: 6.2px; font-weight: 700; line-height: 7.4px; color: var(--charcoal); }

  .brand-word { position: absolute; left: 17px; top: 466px; font-family: "Archivo Black", Arial, sans-serif;
    font-size: 41px; letter-spacing: 0.5px; color: var(--ink); line-height: 44px; }
  .brand-acronym { position: absolute; left: 16px; top: 509px; font-family: "Archivo Black", Arial, sans-serif;
    font-size: 15.5px; line-height: 20px; color: var(--gold-text); }

  .path-list { position: absolute; left: 224px; top: 308px; width: 214px; list-style: none; }
  .path { height: 33px; }
  .path__head { display: flex; align-items: center; gap: 5px; font-family: "Archivo Black", Arial, sans-serif;
    font-size: 11px; letter-spacing: 0.4px; line-height: 13px; border-bottom: 1.5px solid var(--gold); height: 15px; }
  .path__mark { width: 7px; height: 7px; background: var(--gold); border-radius: 1px; margin-left: 2px; }
  .path__title { font-size: 10.3px; font-weight: 500; line-height: 15px; border-bottom: 1.5px solid var(--gold); height: 16px; white-space: nowrap; }
  .module-line { position: absolute; left: 224px; top: 542px; width: 211px; height: 22px;
    border-top: 2.5px solid var(--charcoal); border-bottom: 2.5px solid var(--charcoal);
    font-size: 10.3px; font-weight: 600; line-height: 17px; white-space: nowrap; }
  .module-line b { font-family: "Archivo Black", Arial, sans-serif; font-weight: 400; color: var(--gold-text); margin-right: 4px; }

  /* Back page */
  .gold-field { position: absolute; left: 0; top: 0; width: 446px; height: 354px; background: var(--gold); }
  .framework { position: absolute; left: 0; top: 0; width: 446px; height: 210px; }
  .node { position: absolute; display: flex; align-items: center; justify-content: center; text-align: center; }
  .node--root { left: 152px; top: 16px; width: 140px; height: 34px; background: var(--grey); border: 2px solid var(--charcoal);
    font-family: "Archivo Black", Arial, sans-serif; font-size: 10px; color: var(--charcoal); }
  .node--branch { top: 69px; width: 117px; height: 34px; background: var(--grey-light); border: 2px solid var(--charcoal);
    font-weight: 700; font-size: 8.6px; line-height: 10px; color: var(--charcoal); }
  .node--leaf { width: 96px; height: 22px; background: #fff; border: 2px solid var(--charcoal);
    font-weight: 600; font-size: 6.8px; line-height: 8.2px; color: var(--ink); }

  .shift-band { position: absolute; left: 0; top: 228px; width: 272px; height: 73px; background: var(--charcoal); }
  .shift-quote { position: absolute; left: 15px; top: 239px; font-family: "Oswald", Arial, sans-serif; font-weight: 600;
    font-size: 21px; line-height: 26px; color: var(--gold-text); letter-spacing: -0.2px; }
  .shift-body { position: absolute; left: 17px; top: 312px; width: 245px; font-size: 8.6px; line-height: 10.6px;
    font-weight: 600; color: var(--charcoal); }

  .arch-frame { position: absolute; left: 264px; top: 212px; width: 176px; height: 316px; border-radius: 88px; background: #fff; }
  .arch-photo { position: absolute; left: 275px; top: 222px; width: 154px; height: 296px; border-radius: 77px;
    background: linear-gradient(180deg, #f3d58a 0%, #e7b864 35%, #b88d4f 60%, #6d6a45 85%, #4e5a36 100%); }

  .coach-heading { position: absolute; left: 12px; top: 370px; font-family: "Archivo Black", Arial, sans-serif;
    font-size: 15.2px; letter-spacing: 0.3px; color: var(--ink); }
  .coach-name { position: absolute; left: 12px; top: 390px; width: 178px; font-size: 9.8px; font-weight: 700; line-height: 13px;
    border-top: 1px solid var(--gold); border-bottom: 1px solid var(--gold); }
  .coach-role { position: absolute; left: 12px; top: 407px; font-size: 7.3px; line-height: 8.6px; color: var(--ink); }
  .testimonial { position: absolute; left: 33px; top: 433px; width: 108px; height: 126px;
    border-left: 1px solid var(--charcoal); border-right: 1px solid var(--charcoal);
    font-size: 6.9px; line-height: 8.7px; font-weight: 700; text-align: center; padding: 8px 4px 0; }
  .portrait-ring { position: absolute; left: 164px; top: 409px; width: 108px; height: 148px; border-radius: 50%;
    border: 5px solid var(--charcoal); background: #fff; }
  .portrait-photo { position: absolute; left: 171px; top: 416px; width: 94px; height: 134px; border-radius: 50%;
    background: linear-gradient(170deg, #8a4a3a 0%, #6b3a30 40%, #b8977b 70%, #3d3a3a 100%); }

  .company-mark { position: absolute; left: 333px; top: 478px; width: 44px; height: 44px; border-radius: 50%; background: var(--charcoal); }
  .company-name { position: absolute; left: 290px; top: 526px; width: 132px; text-align: center; font-family: "Archivo", Arial, sans-serif;
    font-weight: 500; font-size: 19px; color: var(--charcoal); }
  .company-url { position: absolute; left: 290px; top: 551px; width: 132px; text-align: center; font-size: 7.6px; color: var(--gold-text); }
</style>
</head>
<body>

<section class="page page--front">
  <header class="hero">
    <div class="hero__photo" role="img" aria-label="Photo of a worried young man in a blue sweater counting cash at a desk"></div>
    <h1 class="hero__headline">How much is<br>chronic stress<br>and burnout<br>costing your<br>organization?</h1>
    <p class="hero__lede">Reduce healthcare costs by providing knowledge, tools and techniques to increase employee self-awareness and self-agency.</p>
  </header>

  <div class="benefit-band">
    <div class="benefit">
      <svg class="benefit__icon" viewBox="0 0 29 29"><rect width="29" height="29" rx="5" fill="#3a3a3a"/><path d="M16 5 L9 16 H14 L12 24 L20 12 H15 Z" fill="#dfc35a"/></svg>
      <span class="benefit__label">Reduce employee<br>Burnout</span>
    </div>
    <div class="benefit">
      <svg class="benefit__icon" viewBox="0 0 29 29"><rect width="29" height="29" rx="5" fill="#3a3a3a"/><g fill="#fff"><rect x="7" y="16" width="3" height="6"/><rect x="12" y="15" width="3" height="3"/><rect x="17" y="12" width="3" height="3"/><rect x="21" y="8" width="3" height="6"/></g></svg>
      <span class="benefit__label">Reduce healthcare<br>costs</span>
    </div>
    <div class="benefit">
      <svg class="benefit__icon" viewBox="0 0 29 29"><rect width="29" height="29" rx="5" fill="#3a3a3a"/><polyline points="4,18 10,11 17,17 25,9" fill="none" stroke="#fff" stroke-width="2"/><g fill="#fff"><circle cx="10" cy="11" r="2"/><circle cx="17" cy="17" r="2"/></g></svg>
      <span class="benefit__label">Reduce turnover<br>and absenteeism</span>
    </div>
  </div>

  <div class="pathways-tab">Pathways to Implementation</div>

  <svg class="benefits-chart" viewBox="0 0 194 194" aria-label="Program benefits chart">
    <defs><path id="costs-arc" d="M38 97 A59 59 0 0 1 95 38"/></defs>
    <g fill="none">
      <path d="M38 97 A59 59 0 0 1 95 38" stroke="#3a3a3a" stroke-width="28"/>
      <path d="M99 38 A59 59 0 0 1 143.5 60.7" stroke="#dfc35a" stroke-width="28"/>
      <path d="M145.3 63.1 A59 59 0 0 1 154 81.7" stroke="#7b7b7d" stroke-width="20"/>
      <path d="M154.7 84.7 A59 59 0 0 1 143.5 133.3" stroke="#dfc35a" stroke-width="28"/>
      <path d="M141.5 135.7 A59 59 0 0 1 126.5 148.1" stroke="#7b7b7d" stroke-width="20"/>
      <path d="M123.8 149.6 A59 59 0 0 1 47 128.3" stroke="#dfc35a" stroke-width="28"/>
      <path d="M45.4 125.6 A59 59 0 0 1 38.1 100.1" stroke="#7b7b7d" stroke-width="20"/>
    </g>
    <text font-family="Archivo, Arial, sans-serif" font-size="10.5" font-weight="500" fill="#fff" dominant-baseline="central">
      <textPath href="#costs-arc" startOffset="50%" text-anchor="middle">Program Costs</textPath>
    </text>
    <circle cx="97" cy="97" r="44" fill="#fff"/>
    <circle cx="97" cy="97" r="39" fill="#7b7b7d" stroke="#c9c9cb" stroke-width="2.5"/>
    <text x="97" y="93" text-anchor="middle" font-family="Oswald, Arial, sans-serif" font-weight="600" font-size="11" fill="#fff">Program</text>
    <text x="97" y="107" text-anchor="middle" font-family="Oswald, Arial, sans-serif" font-weight="600" font-size="11" fill="#fff">Benefits</text>
    <g stroke="#dfc35a" stroke-width="0.8" fill="#dfc35a">
      <line x1="149" y1="72" x2="171" y2="56"/><circle cx="149" cy="72" r="3" stroke="none"/>
      <line x1="138" y1="143" x2="152" y2="150"/><circle cx="138" cy="143" r="3" stroke="none"/>
      <line x1="48" y1="128" x2="34" y2="142"/><circle cx="48" cy="128" r="3" stroke="none"/>
    </g>
  </svg>
  <span class="chart-label" style="left:169px;top:304px">Reduced<br>Healthcare<br>costs</span>
  <span class="chart-label" style="left:158px;top:429px;text-align:center">Decreased<br>Absenteeism</span>
  <span class="chart-label" style="left:11px;top:431px;text-align:center">Increased<br>Productivity</span>

  <div class="brand-word">TALON</div>
  <p class="brand-acronym">Tracks Across Life,<br>Openness and<br>Nurture</p>

  <ol class="path-list">
    <li class="path"><div class="path__head"><span class="path__mark"></span>TALON Path 1</div><div class="path__title">The Power of Emotional Regulation</div></li>
    <li class="path"><div class="path__head"><span class="path__mark"></span>TALON Path 2</div><div class="path__title">Getting in Sync with Your Heart’s Wisdom</div></li>
    <li class="path"><div class="path__head"><span class="path__mark"></span>TALON Path 3</div><div class="path__title">Shifting from Disempowered to Empowered</div></li>
    <li class="path"><div class="path__head"><span class="path__mark"></span>TALON Path 4</div><div class="path__title">Building a Foundation of Coherence</div></li>
    <li class="path"><div class="path__head"><span class="path__mark"></span>TALON Path 5</div><div class="path__title">The Power of What You Believe</div></li>
    <li class="path"><div class="path__head"><span class="path__mark"></span>TALON Path 6</div><div class="path__title">The Power of Your Thoughts</div></li>
    <li class="path"><div class="path__head"><span class="path__mark"></span>TALON Path 7</div><div class="path__title">The Power of Your Subconscious Mind</div></li>
  </ol>
  <div class="module-line"><b>Module 8:</b>Stepping into Your TALON</div>
</section>

<section class="page page--back">
  <div class="gold-field"></div>

  <svg class="framework" viewBox="0 0 446 210" aria-hidden="true">
    <g stroke="#3a3a3a" stroke-width="2" fill="none">
      <path d="M222 50 V60 M83 60 H362 M83 59 V69 M222 60 V69 M362 59 V69"/>
      <path d="M33 103 V190 M33 128 H46 M33 159 H46 M33 190 H46"/>
      <path d="M172 103 V190 M172 128 H185 M172 159 H185 M172 190 H185"/>
      <path d="M311 103 V190 M311 128 H324 M311 159 H324 M311 190 H324"/>
    </g>
  </svg>
  <div class="node node--root">The TALON Program</div>
  <div class="node node--branch" style="left:25px">Learning &amp;<br>Development</div>
  <div class="node node--branch" style="left:164px">Personalized Support<br>and Coaching</div>
  <div class="node node--branch" style="left:303px">Resources and<br>Engagement Tools</div>

  <div class="node node--leaf" style="left:46px;top:117px">Online Courses</div>
  <div class="node node--leaf" style="left:46px;top:148px">Monthly Topic -<br>Specific Workshops</div>
  <div class="node node--leaf" style="left:46px;top:179px">Book Study Program</div>
  <div class="node node--leaf" style="left:185px;top:117px">Individual Assessments<br>and Reporting</div>
  <div class="node node--leaf" style="left:185px;top:148px">Group Coaching</div>
  <div class="node node--leaf" style="left:185px;top:179px">1:1 Coaching</div>
  <div class="node node--leaf" style="left:324px;top:117px">Promotional<br>Newsletters/Emails</div>
  <div class="node node--leaf" style="left:324px;top:148px">Workplace<br>Posters/Flyers</div>
  <div class="node node--leaf" style="left:324px;top:179px">Online Toolkit</div>

  <div class="shift-band"></div>
  <p class="shift-quote">"This is not just a program.<br>It's a paradigm shift."</p>
  <p class="shift-body">Through The TALON Program, participants learn not only how to manage stress, but to deeply understand how stress impacts their body and their mind.</p>

  <div class="arch-frame"></div>
  <div class="arch-photo" role="img" aria-label="Photo of a woman in a yoga pose by a lake at sunset, seen from behind"></div>

  <h2 class="coach-heading">EXECUTIVE COACH &amp; ADVISOR</h2>
  <p class="coach-name">Maren Holt, Founder BrindleCove LLC</p>
  <p class="coach-role">Experienced Executive Coach and Advisor:<br>Transforming Leaders and Teams.</p>
  <blockquote class="testimonial">“Maren taught me a new way of leading others through mindfulness and compassion, where we worked as a team, rather than simply managing people and delegating tasks. The result was my team felt valued and had meaningful purpose. I became a better leader of people through Maren’s guidance.”</blockquote>

  <div class="portrait-ring"></div>
  <div class="portrait-photo" role="img" aria-label="Portrait photo of the founder seated by a brick fireplace"></div>

  <div class="company-mark"></div>
  <div class="company-name">BrindleCove</div>
  <div class="company-url">www.brindlecove.com</div>
</section>

</body>
</html>
```